Breezy Lanterns Handcrafted Copper Jewelry

I make handcrafted copper bracelets and cuffs.
I need a banner made (2' 1/2" x 10')
I attached the logo (I would like that sketch to be purple)
Company name: Breezy Lanterns (in a "sassy" font)
Tag line: Bring the Breeze
Designer/Creator: Marla Dunsby
481.307.6624
PN: www.pagenook.com/breezylanterns.net
shop.breezylanterns.net
I'd like the background to be white. I'm not sure what I'm looking for as far as the look or if I should add any pics of the copper jewelry that I make. I'm totally up for suggestions. I'm very eager to see how creative you can be.
Many thanks.

```html
<!DOCTYPE html>
<html lang="en">
<head>
<meta charset="utf-8">
<title>Breezy Lanterns Banner</title>
<link rel="stylesheet" href="https://fonts.googleapis.com/css2?family=Sofia&family=Tinos&display=swap">
<style>
  :root {
    --bg-center: #ffffff;
    --bg-edge: #cdcdcd;
    --title-grey: #5a5a5a;
    --ink: #111111;
    --rule-grey: #9a9a9a;
    --sketch-light: #fbe3d2;
    --sketch-mid: #f4b383;
  }
  html, body {
    margin: 0;
    padding: 0;
    overflow: hidden;
    background: #ffffff;
  }
  .banner {
    position: relative;
    width: 1200px;
    height: 307px;
    overflow: hidden;
    background: radial-gradient(ellipse 60% 90% at 50% 45%, var(--bg-center) 0%, #f3f3f3 45%, var(--bg-edge) 100%);
  }
  .banner__rule {
    position: absolute;
    left: 0;
    right: 0;
    bottom: 2px;
    height: 4px;
    background: var(--rule-grey);
  }
  .banner__figure {
    position: absolute;
    left: 208px;
    top: 18px;
    width: 132px;
    height: 258px;
    border-radius: 40px 40px 10px 10px;
    background: linear-gradient(180deg, var(--sketch-light) 0%, var(--sketch-mid) 45%, var(--sketch-light) 100%);
  }
  .banner__name {
    position: absolute;
    left: 364px;
    top: 76px;
    margin: 0;
    font-family: "Sofia", cursive;
    font-weight: 400;
    font-size: 96px;
    letter-spacing: -2px;
    line-height: 1;
    color: var(--title-grey);
    white-space: nowrap;
  }
  .banner__tagline {
    position: absolute;
    left: 898px;
    top: 168px;
    margin: 0;
    font-family: "Sofia", cursive;
    font-size: 15px;
    line-height: 1;
    color: var(--ink);
    white-space: nowrap;
  }
  .banner__contact {
    position: absolute;
    left: 442px;
    top: 203px;
    width: 560px;
    margin: 0;
    text-align: center;
    font-family: "Tinos", serif;
    font-size: 16px;
    line-height: 23px;
    color: var(--ink);
  }
  .banner__contact p {
    margin: 0;
    white-space: nowrap;
  }
</style>
</head>
<body>
  <div class="banner">
    <div class="banner__figure" role="img" aria-label="Orange line sketch of a woman in a flowing strapless dress"></div>
    <h1 class="banner__name">Breezy Lanterns</h1>
    <p class="banner__tagline">Bring the Breeze</p>
    <div class="banner__contact">
      <p>Designer: Marla Dunsby</p>
      <p>481.307.6624</p>
      <p>PN: www.pagenook.com/breezylanterns.net</p>
      <p>shop.breezylanterns.net</p>
    </div>
    <div class="banner__rule"></div>
  </div>
</body>
</html>
```